Lien Post Card - (5.5 x 8.5)

FRONT OF POSTCARD
Is a Property Lien Putting Your Home at Risk?
HOA Liens • Tax Liens • Municipal Charges • Other Property-Related Liens
You may have options to resolve outstanding liens and protect your home.
A Refinance or Home Equity Line of Credit (HELOC) may help you:
✔ Pay off qualifying liens
✔ Consolidate debt into one manageable payment
✔ Access your home's equity
✔ Improve your financial flexibility
✔ Avoid additional penalties, fees, or collection actions
Don't wait until the situation becomes more difficult.
Call today for a confidential review of your options.
Bluegate Lending Partners, Inc.
(800) 647-2915 x 42
www.bluegatelendco.com
NMLS #381640
BACK OF POSTCARD
Your Home Equity Could Be the Solution
If you have received notices regarding:
• Delinquent Property Taxes
• HOA or Condo Association Assessments
• Municipal Utility Liens
• Special Assessments
• Other Property-Related Obligations
You may qualify for financing options designed to help satisfy those obligations and bring your property current.
Our experienced mortgage professionals can review your situation and discuss available programs, including:
• Cash-Out Refinancing
• Home Equity Lines of Credit (HELOCs)
• Home Equity Loans
• Debt Consolidation Solutions
Free Consultation • No Obligation
Contact Marcus Delaney today at (800) 647-2915 x42 or mdelaney@bluegatelendco.com (NMLS #57308)

```html
<!DOCTYPE html>
<html lang="en">
<head>
<meta charset="utf-8">
<title>Lien Postcard – Front and Back</title>
<link href="https://fonts.googleapis.com/css2?family=Figtree:wght@400;500;600;700;800&family=Bebas+Neue&display=swap" rel="stylesheet">
<style>
  :root{
    --page:#dcdcdc;
    --ink:#0b0b0c;
    --blue:#0b5a8c;
    --blue-bright:#1d8fd0;
    --gold:#b8a431;
    --gold-text:#c9b13b;
    --pale-gold:#e3d79a;
    --green:#8cc63f;
    --navy:#0f4c86;
    --white:#ffffff;
    --grey-text:#2b2b2b;
  }
  *{box-sizing:border-box;margin:0;padding:0}
  html,body{width:1143px;height:1200px;overflow:hidden}
  body{background:var(--page);font-family:"Figtree",sans-serif;position:relative}
  .card{position:absolute;left:198px;width:747px;height:498px;overflow:hidden;box-shadow:0 6px 18px rgba(0,0,0,.25)}
  .card--front{top:71px;background:var(--ink)}
  .card--back{top:616px;background:var(--white)}
  .abs{position:absolute}
  .deco{position:absolute;inset:0;width:747px;height:498px}

  /* front */
  .front-texture{position:absolute;inset:0;background:linear-gradient(180deg,#1a1b1d 0%,#0d0d0e 45%,#202224 100%)}
  .brand-box{left:60px;top:4px;width:207px;height:142px;background:#0c0d10;display:flex;align-items:center;justify-content:center;gap:8px}
  .brand-name{font-weight:700;color:var(--gold-text);font-size:19px;line-height:1.15;text-align:center}
  .brand-mark{width:12px;height:12px;border-radius:50%;background:var(--gold-text);flex:none}
  .headline{left:52px;top:155px;font-weight:800;font-size:30px;line-height:31.5px;color:var(--white);letter-spacing:.2px}
  .headline .accent{color:var(--gold-text)}
  .lien-types{left:52px;top:259px;width:290px;font-weight:600;font-size:15.5px;line-height:18.5px;color:var(--white)}
  .rule{left:52px;top:311px;width:46px;height:2px;background:var(--green)}
  .front-lede{left:52px;top:324px;width:310px;font-size:13.4px;line-height:16.5px;color:var(--white)}
  .benefits{left:378px;top:203px;width:352px;height:157px;border:1.5px solid var(--gold);border-radius:10px;background:rgba(0,0,0,.82);padding:11px 14px}
  .benefits h2{font-weight:800;font-size:15px;line-height:18px;color:var(--white);margin-bottom:5px}
  .tick-list{list-style:none}
  .tick-list li{display:flex;align-items:center;gap:8px;color:var(--white);font-size:13px;line-height:18.3px;white-space:nowrap}
  .tick{width:11px;height:11px;flex:none}
  .cta-kicker{left:0;width:747px;top:400px;text-align:center;color:var(--white);font-size:11px;letter-spacing:.1px}
  .cta-main{left:0;width:747px;top:414px;text-align:center;color:var(--white);font-weight:800;font-size:16.5px}
  .footer-bar{left:0;top:450px;width:747px;height:48px;background:var(--gold);display:flex;align-items:center;justify-content:center;color:var(--white);font-weight:600;font-size:14px}

  /* back */
  .back-title{left:32px;top:120px;font-family:"Bebas Neue",sans-serif;font-size:27px;letter-spacing:.2px;color:var(--pale-gold);white-space:nowrap}
  .back-title .accent{color:var(--green)}
  .notice-intro{left:32px;top:153px;font-weight:700;font-size:12.5px;color:var(--white)}
  .notice-list{left:32px;top:170px;list-style:none}
  .notice-list li{font-size:10.8px;line-height:14.3px;color:var(--white);padding-left:11px;position:relative}
  .notice-list li::before{content:"";position:absolute;left:0;top:5.5px;width:3.5px;height:3.5px;border-radius:50%;background:var(--green)}
  .back-lede{left:32px;top:245px;width:340px;font-weight:500;font-size:12px;line-height:14px;color:var(--white)}
  .programs{left:32px;top:302px;width:313px;height:100px;border:1.5px solid var(--gold);border-radius:8px;background:var(--white);padding:10px 13px}
  .programs p{font-weight:700;font-size:11px;line-height:13.5px;color:var(--navy);margin-bottom:7px}
  .program-grid{display:grid;grid-template-columns:170px 1fr;row-gap:5px;list-style:none}
  .program-grid li{display:flex;gap:6px;font-size:11px;line-height:11.5px;color:var(--grey-text)}
  .program-grid .tick{width:9px;height:9px;margin-top:1px}
  .contact-band{left:0;top:415px;width:352px;height:83px;background:var(--blue)}
  .consult-badge{left:32px;top:432px;width:122px;height:49px;border:1.5px solid var(--gold);border-radius:4px;font-family:"Bebas Neue",sans-serif;color:var(--white);text-align:center;line-height:1}
  .consult-badge .small{display:block;font-size:16px;margin-top:6px}
  .consult-badge .big{display:block;font-size:21px}
  .contact{left:171px;top:434px;width:172px;color:var(--white);white-space:nowrap}
  .contact .lead{font-size:8.5px}
  .contact .phone{display:flex;align-items:center;gap:3px;font-weight:700;font-size:15px;margin-top:2px}
  .contact .email{display:flex;align-items:center;gap:5px;font-size:9.5px;margin-top:1px}
  .contact .nmls{font-size:8px;margin-top:4px}
  .portrait{left:354px;top:298px;width:132px;height:200px;border-radius:44px 44px 0 0;background:linear-gradient(180deg,#2a2a2c,#0e0e10)}
  .back-brand{left:455px;top:40px;width:150px;text-align:center;font-weight:700;font-size:16px;line-height:19px;color:var(--navy)}
  .stamp{left:644px;top:20px;width:78px;height:80px;background:#d3d4d6}
</style>
</head>
<body>

<section class="card card--front" aria-label="Postcard front">
  <div class="front-texture" role="img" aria-label="Dark, faded photo of a suburban house"></div>
  <svg class="deco" viewBox="0 0 747 498" aria-hidden="true">
    <defs>
      <linearGradient id="photoTone" x1="0" y1="0" x2="0" y2="1">
        <stop offset="0" stop-color="#8f9a93"/>
        <stop offset=".55" stop-color="#6d7274"/>
        <stop offset="1" stop-color="#a9aaa5"/>
      </linearGradient>
    </defs>
    <path d="M255,0 C300,150 470,230 600,222 C680,216 730,190 747,170 L747,0 Z" fill="var(--blue-bright)"/>
    <path d="M272,0 C320,140 470,212 600,205 C680,198 730,170 747,150 L747,0 Z" fill="var(--ink)"/>
    <path d="M300,0 C338,118 460,185 583,180 C662,176 722,140 747,112" fill="none" stroke="var(--gold)" stroke-width="5"/>
  </svg>
  <svg class="deco" viewBox="0 0 747 498" role="img" aria-label="Photo of a stressed man covering his face with his hands">
    <path d="M307,0 C342,112 455,180 580,175 C660,170 720,136 747,106 L747,0 Z" fill="url(#photoTone)"/>
  </svg>

  <div class="abs brand-box">
    <span class="brand-mark"></span>
    <span class="brand-name">Bluegate Lending<br>Partners</span>
  </div>

  <h1 class="abs headline">IS A PROPERTY<br>LIEN PUTTING YOUR<br><span class="accent">HOME AT RISK?</span></h1>
  <p class="abs lien-types">HOA Liens • Tax Liens • Municipal Charges • Other Property-Related Liens</p>
  <div class="abs rule"></div>
  <p class="abs front-lede">You may have options to resolve outstanding liens and protect your home.</p>

  <div class="abs benefits">
    <h2>A REFINANCE OR HOME EQUITY LINE OF CREDIT (HELOC) MAY HELP YOU:</h2>
    <ul class="tick-list">
      <li><svg class="tick" viewBox="0 0 12 12"><circle cx="6" cy="6" r="6" fill="var(--green)"/><path d="M3.2 6.2l1.9 1.9 3.8-3.9" stroke="#000" stroke-width="1.6" fill="none"/></svg>Pay off qualifying liens</li>
      <li><svg class="tick" viewBox="0 0 12 12"><circle cx="6" cy="6" r="6" fill="var(--green)"/><path d="M3.2 6.2l1.9 1.9 3.8-3.9" stroke="#000" stroke-width="1.6" fill="none"/></svg>Consolidate debt into one manageable payment</li>
      <li><svg class="tick" viewBox="0 0 12 12"><circle cx="6" cy="6" r="6" fill="var(--green)"/><path d="M3.2 6.2l1.9 1.9 3.8-3.9" stroke="#000" stroke-width="1.6" fill="none"/></svg>Access your home's equity</li>
      <li><svg class="tick" viewBox="0 0 12 12"><circle cx="6" cy="6" r="6" fill="var(--green)"/><path d="M3.2 6.2l1.9 1.9 3.8-3.9" stroke="#000" stroke-width="1.6" fill="none"/></svg>Improve your financial flexibility</li>
      <li><svg class="tick" viewBox="0 0 12 12"><circle cx="6" cy="6" r="6" fill="var(--green)"/><path d="M3.2 6.2l1.9 1.9 3.8-3.9" stroke="#000" stroke-width="1.6" fill="none"/></svg>Avoid additional penalties, fees, or collection actions</li>
    </ul>
  </div>

  <svg class="deco" viewBox="0 0 747 498" aria-hidden="true">
    <path d="M0,412 Q373,330 747,406 L747,450 L0,450 Z" fill="#1d6fa5"/>
    <path d="M0,420 Q373,338 747,414 L747,450 L0,450 Z" fill="var(--blue)"/>
  </svg>
  <p class="abs cta-kicker">DON'T WAIT UNTIL THE SITUATION BECOMES MORE DIFFICULT.</p>
  <p class="abs cta-main">CALL TODAY FOR A CONFIDENTIAL REVIEW OF YOUR OPTIONS.</p>
  <div class="abs footer-bar">Bluegate Lending Partners, Inc. • (800) 647-2915 x 42 • www.bluegatelendco.com • NMLS #381640</div>
</section>

<section class="card card--back" aria-label="Postcard back">
  <svg class="deco" viewBox="0 0 747 498" aria-hidden="true">
    <defs>
      <radialGradient id="sunset" cx=".55" cy=".7" r=".7">
        <stop offset="0" stop-color="#f2a533"/>
        <stop offset=".35" stop-color="#a45f22"/>
        <stop offset="1" stop-color="#2a2119"/>
      </radialGradient>
      <linearGradient id="skyFade" x1="0" y1="0" x2="0" y2="1">
        <stop offset=".6" stop-color="#000" stop-opacity="0"/>
        <stop offset="1" stop-color="#000" stop-opacity="1"/>
      </linearGradient>
      <clipPath id="panelClip">
        <path d="M0,0 L352,0 C395,90 425,200 428,292 L0,292 Z"/>
      </clipPath>
    </defs>
    <path d="M395,0 C450,120 465,250 440,310 C455,240 440,110 380,0 Z" fill="var(--blue-bright)"/>
    <path d="M360,0 C420,110 445,240 420,360 C410,400 405,430 400,440 C430,330 420,170 345,0 Z" fill="var(--gold)"/>
    <path d="M0,0 L352,0 C395,90 425,200 428,292 L0,292 Z" fill="var(--ink)"/>
  </svg>
  <svg class="deco" viewBox="0 0 747 498" role="img" aria-label="Photo of a city skyline silhouetted against a sunset">
    <g clip-path="url(#panelClip)">
      <rect x="0" y="0" width="430" height="120" fill="url(#sunset)"/>
      <rect x="0" y="0" width="430" height="120" fill="url(#skyFade)"/>
    </g>
  </svg>

  <h2 class="abs back-title">YOUR HOME EQUITY <span class="accent">COULD BE THE SOLUTION</span></h2>
  <p class="abs notice-intro">If you have received notices regarding:</p>
  <ul class="abs notice-list">
    <li>Delinquent Property Taxes</li>
    <li>HOA or Condo Association Assessments</li>
    <li>Municipal Utility Liens</li>
    <li>Special Assessments</li>
    <li>Other Property-Related Obligations</li>
  </ul>
  <p class="abs back-lede">You may qualify for financing options designed to help satisfy those obligations and bring your property current.</p>

  <div class="abs programs">
    <p>Our experienced mortgage professionals can review your situation and discuss available programs, including:</p>
    <ul class="program-grid">
      <li><svg class="tick" viewBox="0 0 12 12"><circle cx="6" cy="6" r="6" fill="var(--green)"/><path d="M3.2 6.2l1.9 1.9 3.8-3.9" stroke="#fff" stroke-width="1.6" fill="none"/></svg>Cash-Out Refinancing</li>
      <li><svg class="tick" viewBox="0 0 12 12"><circle cx="6" cy="6" r="6" fill="var(--green)"/><path d="M3.2 6.2l1.9 1.9 3.8-3.9" stroke="#fff" stroke-width="1.6" fill="none"/></svg>Home Equity Loans</li>
      <li><svg class="tick" viewBox="0 0 12 12"><circle cx="6" cy="6" r="6" fill="var(--green)"/><path d="M3.2 6.2l1.9 1.9 3.8-3.9" stroke="#fff" stroke-width="1.6" fill="none"/></svg><span>Home Equity Lines of Credit (HELOCs)</span></li>
      <li><svg class="tick" viewBox="0 0 12 12"><circle cx="6" cy="6" r="6" fill="var(--green)"/><path d="M3.2 6.2l1.9 1.9 3.8-3.9" stroke="#fff" stroke-width="1.6" fill="none"/></svg><span>Debt Consolidation Solutions</span></li>
    </ul>
  </div>

  <div class="abs contact-band"></div>
  <div class="abs consult-badge"><span class="small">FREE CONSULTATION</span><span class="big">NO OBLIGATION</span></div>
  <div class="abs contact">
    <p class="lead">Contact Marcus Delaney today at</p>
    <p class="phone"><svg width="12" height="12" viewBox="0 0 24 24"><path fill="#fff" d="M6.6 10.8a15.1 15.1 0 0 0 6.6 6.6l2.2-2.2c.3-.3.7-.4 1-.2 1.1.4 2.3.6 3.6.6.6 0 1 .4 1 1V20c0 .6-.4 1-1 1A17 17 0 0 1 3 4c0-.6.4-1 1-1h3.5c.6 0 1 .4 1 1 0 1.3.2 2.5.6 3.6.1.3 0 .7-.2 1z"/></svg>(800) 647-2915 x42</p>
    <p class="email"><svg width="10" height="10" viewBox="0 0 10 10"><circle cx="5" cy="5" r="5" fill="#fff"/><rect x="2.3" y="3.2" width="5.4" height="3.6" fill="none" stroke="var(--blue)" stroke-width=".8"/><path d="M2.3 3.2L5 5.3 7.7 3.2" fill="none" stroke="var(--blue)" stroke-width=".8"/></svg>mdelaney@bluegatelendco.com</p>
    <p class="nmls">(NMLS #57308)</p>
  </div>
  <div class="abs portrait" role="img" aria-label="Photo of the loan officer in a dark hat and coat"></div>

  <div class="abs back-brand">Bluegate Lending Partners</div>
  <div class="abs stamp" aria-label="Postage area"></div>
</section>

</body>
</html>
```